Hard-File Archival Services Billboard (Digitization Service) for Attorneys/Law Firms

I need a billboard design for my company "Keltor Legal Aides" that advertises our primary service: Digitization of closed client files, for law firms and attorneys. Our system works as follows: 1) We get a call about a firm that wants to digitize their archived (closed) client files (which usually find their way to file cabinets or bankers boxes), 2) We go and pick those up from the law firm, 3) We bring them to our digitization facility, scan them in, and convert them into searchable PDF/A files, and 4) We upload them on the cloud, give the client a URL to visit their files whenever they want, and we delete them when requested by the client (usually for the retention duration for Missouri's rules of professional conduct, which is 6 years). It would be really cool to see "Keltor Legal Aides" and the logo clearly on the billboard, some simple sentence relating to "Missouri's best digitizing and cloud storage service for closed client files for attorneys" (or something shorter, you get the point), with maybe a linear set of photos and arrows (as follows 1. A photo of a file cabinet opened with files hanging out of it, 2. an arrow pointing to a person scanning in documents in a big scanner (maybe with a Keltor Legal Aidess logo on it?), 3. An arrow pointing to a "secure" appearing cloud (representing cloud storage), and 4. the client sitting at a computer with an arrow pointing back to the cloud (showing the client is accessing the cloud files through the computer). Our website is www.keltorlegalaides.example if you want to glean any additional information from there. Thanks! Oh yes, I should also say the billboard dimensions (in the event you need this for photo aspect ratio) will be as follows: 14 feet tall by 48 feet wide.
Target Market(s)
Attorneys in Springfield, Missouri
Industry/Entity Type
Legal
Look and feel
Each slider illustrates characteristics of the customer's brand and the style your logo design should communicate.

```html
<!DOCTYPE html>
<html lang="en">
<head>
<meta charset="utf-8">
<title>Keltor Legal Aides – Billboard</title>
<link rel="stylesheet" href="https://fonts.googleapis.com/css2?family=Bebas+Neue&family=Open+Sans:wght@700&display=swap">
<style>
  :root {
    --page-bg: #ffffff;
    --board-top: #f4f5f5;
    --board-bottom: #d3ecf6;
    --ink: #111111;
    --accent-blue: #2f6fbd;
    --cloud-stroke: #2d68b4;
    --connector: #2d68b4;
  }
  * { margin: 0; padding: 0; box-sizing: border-box; }
  html, body {
    width: 1000px;
    height: 1200px;
    overflow: hidden;
    background: var(--page-bg);
  }
  .billboard {
    position: absolute;
    left: 30px;
    top: 463px;
    width: 940px;
    height: 274px;
    background: linear-gradient(180deg, var(--board-top) 0%, var(--board-top) 55%, var(--board-bottom) 100%);
    box-shadow: 0 6px 14px rgba(0,0,0,0.28);
  }
  .brand {
    position: absolute;
    left: 46px;
    top: 30px;
    display: flex;
    align-items: center;
    gap: 12px;
  }
  .brand-mark {
    width: 72px;
    height: 72px;
    border-radius: 50%;
    background: var(--ink);
    flex: none;
  }
  .brand-name {
    font-family: "Open Sans", Arial, sans-serif;
    font-weight: 700;
    font-size: 34px;
    color: var(--ink);
    white-space: nowrap;
  }
  .headline {
    position: absolute;
    right: 40px;
    top: 24px;
    text-align: right;
    font-family: "Bebas Neue", "Arial Narrow", sans-serif;
    font-weight: 400;
    font-size: 29px;
    line-height: 36px;
    color: var(--ink);
    white-space: nowrap;
  }
  .headline .accent { color: var(--accent-blue); }
  .process {
    position: absolute;
    left: 38px;
    top: 136px;
    width: 864px;
    height: 118px;
  }
  .step {
    position: absolute;
    top: 0;
    width: 194px;
    height: 117px;
  }
  .step-1 { left: 0; }
  .step-2 { left: 223px; }
  .step-3 { left: 447px; }
  .step-4 { left: 670px; }
  .connector {
    position: absolute;
    top: 89px;
    width: 30px;
    border-top: 2px dotted var(--connector);
  }
  .connector-1 { left: 192px; }
  .connector-2 { left: 415px; }
  .connector-3 { left: 639px; }
</style>
</head>
<body>
  <section class="billboard">
    <div class="brand">
      <span class="brand-mark"></span>
      <span class="brand-name">Keltor Legal Aides</span>
    </div>

    <h1 class="headline">
      Missouri's best <span class="accent">digitizing and</span><br>
      <span class="accent">cloud storage</span> service for closed<br>
      client files <span class="accent">for attorneys</span>
    </h1>

    <div class="process">
      <svg width="0" height="0" style="position:absolute">
        <defs>
          <clipPath id="cloud-shape">
            <path d="M45 188 Q6 188 6 150 Q6 110 52 106 Q62 14 150 12 Q216 12 236 74 Q264 54 292 80 Q314 102 306 140 Q322 160 312 178 Q302 190 280 188 Z"/>
          </clipPath>
          <linearGradient id="cabinet-wood" x1="0" y1="0" x2="1" y2="0">
            <stop offset="0" stop-color="#d9c4a2"/>
            <stop offset="0.55" stop-color="#d8b68a"/>
            <stop offset="1" stop-color="#c9a675"/>
          </linearGradient>
          <linearGradient id="cabinet-floor" x1="0" y1="0" x2="0" y2="1">
            <stop offset="0" stop-color="#c09362" stop-opacity="0"/>
            <stop offset="0.6" stop-color="#b58a5c"/>
            <stop offset="1" stop-color="#2b2b2b"/>
          </linearGradient>
          <linearGradient id="scanner-room" x1="0" y1="0" x2="1" y2="0">
            <stop offset="0" stop-color="#e6d8bd"/>
            <stop offset="0.35" stop-color="#efe9df"/>
            <stop offset="1" stop-color="#d9d9d9"/>
          </linearGradient>
          <linearGradient id="scanner-body" x1="0" y1="0" x2="0" y2="1">
            <stop offset="0" stop-color="#3a3a3a" stop-opacity="0"/>
            <stop offset="0.4" stop-color="#2c2c2c"/>
            <stop offset="1" stop-color="#141414"/>
          </linearGradient>
          <radialGradient id="secure-cloud-glow" cx="0.5" cy="0.35" r="0.6">
            <stop offset="0" stop-color="#e8f7fd"/>
            <stop offset="0.45" stop-color="#8ccbe3"/>
            <stop offset="1" stop-color="#3c86a8"/>
          </radialGradient>
          <linearGradient id="secure-laptop" x1="0" y1="0" x2="0" y2="1">
            <stop offset="0" stop-color="#27607d" stop-opacity="0"/>
            <stop offset="0.6" stop-color="#2f6f8e"/>
            <stop offset="1" stop-color="#1d4358"/>
          </linearGradient>
          <linearGradient id="client-room" x1="0" y1="0" x2="0" y2="1">
            <stop offset="0" stop-color="#f2f2f2"/>
            <stop offset="0.72" stop-color="#e4e4e4"/>
            <stop offset="0.74" stop-color="#d6d6d6"/>
            <stop offset="1" stop-color="#cfcfcf"/>
          </linearGradient>
        </defs>
      </svg>

      <svg class="step step-1" viewBox="0 0 325 195" role="img" aria-label="Photo of an open wooden file cabinet with colored hanging client files">
        <g clip-path="url(#cloud-shape)">
          <rect width="325" height="195" fill="url(#cabinet-wood)"/>
          <rect width="325" height="195" fill="url(#cabinet-floor)"/>
        </g>
        <path d="M45 188 Q6 188 6 150 Q6 110 52 106 Q62 14 150 12 Q216 12 236 74 Q264 54 292 80 Q314 102 306 140 Q322 160 312 178 Q302 190 280 188 Z" fill="none" stroke="var(--cloud-stroke)" stroke-width="5"/>
      </svg>
      <span class="connector connector-1"></span>

      <svg class="step step-2" viewBox="0 0 325 195" role="img" aria-label="Photo of a person feeding documents into a large office scanner">
        <g clip-path="url(#cloud-shape)">
          <rect width="325" height="195" fill="url(#scanner-room)"/>
          <rect x="110" width="215" height="195" fill="url(#scanner-body)"/>
        </g>
        <path d="M45 188 Q6 188 6 150 Q6 110 52 106 Q62 14 150 12 Q216 12 236 74 Q264 54 292 80 Q314 102 306 140 Q322 160 312 178 Q302 190 280 188 Z" fill="none" stroke="var(--cloud-stroke)" stroke-width="5"/>
      </svg>
      <span class="connector connector-2"></span>

      <svg class="step step-3" viewBox="0 0 325 195" role="img" aria-label="Photo of a hand on a laptop under a glowing secure cloud with a lock and upload arrows">
        <g clip-path="url(#cloud-shape)">
          <rect width="325" height="195" fill="url(#secure-cloud-glow)"/>
          <rect width="325" height="195" fill="url(#secure-laptop)"/>
        </g>
        <path d="M45 188 Q6 188 6 150 Q6 110 52 106 Q62 14 150 12 Q216 12 236 74 Q264 54 292 80 Q314 102 306 140 Q322 160 312 178 Q302 190 280 188 Z" fill="none" stroke="var(--cloud-stroke)" stroke-width="5"/>
      </svg>
      <span class="connector connector-3"></span>

      <svg class="step step-4" viewBox="0 0 325 195" role="img" aria-label="Photo of a client in a suit seated in a white chair working on a laptop">
        <g clip-path="url(#cloud-shape)">
          <rect width="325" height="195" fill="url(#client-room)"/>
        </g>
        <path d="M45 188 Q6 188 6 150 Q6 110 52 106 Q62 14 150 12 Q216 12 236 74 Q264 54 292 80 Q314 102 306 140 Q322 160 312 178 Q302 190 280 188 Z" fill="none" stroke="var(--cloud-stroke)" stroke-width="5"/>
      </svg>
    </div>
  </section>
</body>
</html>
```